Identity Card Document Design

Looking for high quality identity card designs for templates.
Please read the detailed brief document which has sample designs and loads of info.
Instant Rejections :
1 You must NOT make anything illegal - anything which looks identical to an existing document. Create an ID card design entirely from scratch. Read the document for more info.
2 The artwork *has* to be provided as per the artwork specs in the document, as a print ready PDF to our size requirements.
3 No gen AI rubbish, don't waste your time, don't waste ours.
Question : In the document, there are certain letters which spell out a specific thing - what is this word? Please submit this word with your design.

```html
<!DOCTYPE html>
<html lang="en">
<head>
<meta charset="utf-8">
<title>Identity Card Template</title>
<link rel="stylesheet" href="https://fonts.googleapis.com/css2?family=Archivo:wght@400;500;600&family=Kaushan+Script&display=swap">
<style>
  :root {
    --page-bg: #c4c4c4;
    --card-blue: #2a3a8e;
    --card-violet: #6a2e80;
    --card-magenta: #a01e60;
    --ink: #ffffff;
    --photo-fill: #c8c8c8;
  }
  html, body {
    margin: 0;
    width: 1200px;
    height: 1200px;
    overflow: hidden;
    background: var(--page-bg);
  }
  .id-card {
    position: absolute;
    left: 110px;
    top: 278px;
    width: 980px;
    height: 645px;
    background: linear-gradient(90deg, var(--card-blue) 0%, var(--card-violet) 50%, var(--card-magenta) 100%);
    box-shadow: 6px 8px 10px rgba(0, 0, 0, 0.28);
    color: var(--ink);
    font-family: "Archivo", Arial, sans-serif;
  }
  .field-label,
  .field-value,
  .address-line {
    position: absolute;
    margin: 0;
    line-height: 1;
    white-space: nowrap;
  }
  .holder-details .field-label,
  .holder-details .field-value,
  .holder-details .address-line { left: 119px; }
  .field-label {
    font-size: 15px;
    font-weight: 500;
    letter-spacing: 0.2px;
  }
  .field-value {
    font-size: 26px;
    font-weight: 600;
    letter-spacing: 0.3px;
  }
  .address-line {
    font-size: 16px;
    font-weight: 600;
  }
  .photo-slot {
    position: absolute;
    left: 700px;
    top: 92px;
    width: 161px;
    height: 181px;
    border-radius: 20px;
    background: var(--photo-fill);
  }
  .card-meta .field-label,
  .card-meta .field-value,
  .card-signature {
    right: 119px;
    text-align: right;
  }
  .card-number { font-size: 27px; font-weight: 500; letter-spacing: 0.5px; }
  .card-signature {
    position: absolute;
    margin: 0;
    top: 549px;
    font-family: "Kaushan Script", cursive;
    font-size: 40px;
    line-height: 1;
  }
</style>
</head>
<body>
  <section class="id-card" aria-label="Identity card">
    <div class="holder-details">
      <p class="field-label" style="top:50px">FIRST NAME (S)</p>
      <p class="field-value" style="top:76px">MARLO</p>
      <p class="field-label" style="top:125px">SURNAME</p>
      <p class="field-value" style="top:152px">FENWICK</p>
      <p class="field-label" style="top:202px">DATE OF BIRTH</p>
      <p class="field-value" style="top:230px">31/12/1900</p>
      <p class="field-label" style="top:279px">PLACE OF STUDY</p>
      <p class="field-value" style="top:306px">PLACEOFSTUDY</p>
      <p class="field-label" style="top:355px">PLACE OF BIRTH</p>
      <p class="field-value" style="top:383px">PLACEOFBIRTH</p>
      <p class="field-label" style="top:431px">MRZ CONCATENATION</p>
      <p class="field-value" style="top:459px">&lt;MRZ&lt;AREA&lt;</p>
      <p class="field-label" style="top:509px">ADDRESS</p>
      <p class="address-line" style="top:531px">14 ASHGROVE LANE, BRIARWOOD,</p>
      <p class="address-line" style="top:553px">NEW SOUTH WALES, POSTCODE,</p>
      <p class="address-line" style="top:576px">AUSTRALIA</p>
    </div>

    <div class="photo-slot" role="img" aria-label="Cardholder photograph"></div>

    <div class="card-meta">
      <p class="field-label" style="top:337px">CARD NUMBER</p>
      <p class="field-value card-number" style="top:366px">1002 3456 - 22 22 22</p>
      <p class="field-label" style="top:510px">CARDHOLDER SIGNATURE</p>
      <p class="card-signature">Signature</p>
    </div>
  </section>
</body>
</html>
```